Letterhead to Introduce a 'Sister' Company.

What I am needing is a design for a letter head to introduce our current customers base of (KT Alarm) customers to our new service, 'Kestrel Tide Solar Brokers'

```html
<!DOCTYPE html>
<html lang="en">
<head>
<meta charset="utf-8">
<title>Kestrel Tide Solar Brokers – Letterhead</title>
<link rel="stylesheet" href="https://fonts.googleapis.com/css2?family=Montserrat:wght@600;700&display=swap">
<style>
  :root {
    --navy: #2e5282;
    --orange: #f9a032;
    --paper: #ffffff;
    --backdrop: #f0f0f0;
  }
  * { margin: 0; padding: 0; box-sizing: border-box; }
  html, body {
    width: 1134px;
    height: 1200px;
    overflow: hidden;
    background: var(--backdrop);
  }
  .letterhead {
    position: absolute;
    left: 157px;
    top: 20px;
    width: 820px;
    height: 1160px;
    background: var(--paper);
    overflow: hidden;
  }
  .letterhead__art {
    position: absolute;
    inset: 0;
    width: 100%;
    height: 100%;
  }
  .header-band { fill: var(--navy); }
  .header-swoosh { fill: var(--orange); }
  .footer-band { fill: var(--navy); }

  .parent-brand {
    position: absolute;
    left: 77px;
    top: 36px;
    font-family: "Montserrat", sans-serif;
    font-weight: 600;
    font-size: 24px;
    letter-spacing: 1px;
    color: var(--paper);
  }

  .company-brand {
    position: absolute;
    left: 515px;
    top: 62px;
    width: 260px;
    text-align: center;
    font-family: "Montserrat", sans-serif;
    font-weight: 700;
    color: var(--navy);
  }
  .company-brand__mark {
    display: block;
    width: 52px;
    height: 52px;
    margin: 0 auto 12px;
    border-radius: 50%;
    background: var(--orange);
  }
  .company-brand__name {
    display: block;
    font-size: 27px;
    line-height: 1;
    letter-spacing: 0.5px;
  }
  .company-brand__tagline {
    display: block;
    margin-top: 6px;
    font-size: 11px;
    letter-spacing: 3px;
  }
</style>
</head>
<body>
  <main class="letterhead">
    <svg class="letterhead__art" viewBox="0 0 1157 1635" preserveAspectRatio="none" aria-hidden="true">
      <path class="header-band" d="M0,0 H1157 V47 C1000,15 500,20 0,225 Z"/>
      <path class="header-swoosh" d="M0,225 C500,20 1000,15 1157,47 C1000,35 500,45 0,262 Z"/>
      <rect class="footer-band" x="0" y="1608" width="1157" height="27"/>
    </svg>

    <div class="parent-brand">KT Alarm</div>

    <div class="company-brand">
      <span class="company-brand__mark"></span>
      <span class="company-brand__name">KESTREL TIDE</span>
      <span class="company-brand__tagline">SOLAR BROKERS</span>
    </div>
  </main>
</body>
</html>
```